Web Design Project

Kluvora.com is an online forum for chatting with friends whilst watching TV. We have attached our wireframes, which we would like a design for. The target audience are 11-40 years old.
Please see similar sites (eg Pollent) for inspiration.
Updates

Target Market(s)

11 to 40 year olds, TV viewers

Industry/Entity Type

Tv

Requirements
Must have
• All the pages and elements included in the wireframes.
Nice to have
• Bold graphical elements.

```html
<!DOCTYPE html>
<html lang="en">
<head>
<meta charset="utf-8">
<title>Kluvora – Home</title>
<link href="https://fonts.googleapis.com/css2?family=Source+Sans+3:wght@400;600&family=Arimo:wght@400&display=swap" rel="stylesheet">
<style>
:root{
  --page:#ececec;
  --white:#ffffff;
  --ink:#222222;
  --muted:#555555;
  --soft:#888888;
  --line:#d6d6d6;
  --green:#7dc324;
  --green-dark:#5e9c16;
  --red:#8b1a1a;
  --grid-bg:#c9c9c9;
  --black:#111111;
  --yellow:#f7b52b;
  --link:#c1121c;
}
*{box-sizing:border-box;margin:0;padding:0}
html,body{width:935px;height:1200px;overflow:hidden}
body{position:relative;background:var(--page);font-family:"Source Sans 3",Arial,sans-serif;color:var(--ink);font-size:12px}
.abs{position:absolute}

.header{left:0;top:0;width:935px;height:98px;background:linear-gradient(#f7f7f7,#ececec)}
.brand{left:47px;top:8px;width:108px;height:70px;border:5px solid var(--black);border-radius:6px;background:var(--white);display:flex;align-items:center;justify-content:center;font-size:20px;color:var(--ink)}
.search{left:639px;top:24px;width:280px;height:21px;display:flex}
.search input{flex:1;border:1px solid var(--line);background:var(--white);font:11px "Source Sans 3",sans-serif;padding:0 10px;color:var(--soft)}
.search button{width:60px;border:0;background:linear-gradient(#4a4a4a,#1e1e1e);color:var(--white);font:12px "Source Sans 3",sans-serif}
.account{right:20px;top:61px;font-size:11.5px;color:var(--muted)}
.account span{margin:0 7px}

.nav{left:0;top:98px;width:935px;height:39px;background:linear-gradient(#8fd136,var(--green) 60%,var(--green-dark));display:flex;align-items:stretch}
.nav a{color:var(--white);text-decoration:none;font-size:14px;display:flex;align-items:center;margin-left:31px}
.nav a.active{background:var(--white);color:var(--ink);margin-left:22px;padding:0 15px}
.nav a.first{margin-left:38px}

.panel{left:17px;top:152px;width:904px;height:995px;background:var(--white);border-radius:3px;box-shadow:0 0 4px rgba(0,0,0,.25)}

.hero{left:32px;top:169px;width:598px;height:283px;background:#f1f1f1;border:1px solid #e2e2e2;border-radius:3px}
.hero-photo{left:40px;top:173px;width:583px;height:217px;background:radial-gradient(ellipse at 40% 30%,#6a2d22,#2a1410 55%,#120a08)}
.hero-bar{left:40px;top:390px;width:583px;height:59px;background:var(--black);color:#cfcfcf}
.hero-bar .title{left:18px;top:18px;font-size:13px}
.hero-bar .meta{left:18px;top:38px;font-size:13px}
.hero-bar .meta span{margin:0 10px}
.pill{font-size:8px;background:#dfe6f2;color:#3b5998;border-radius:2px;padding:1px 4px}
.count{font-size:7px;background:var(--white);color:#333;border:1px solid #bbb;padding:0 2px;margin-left:3px}
.shares{left:506px;top:14px;display:flex;flex-direction:column;gap:6px}
.shares div{display:flex;align-items:center}
.arrow-btn{width:20px;height:34px;background:var(--white);display:flex;align-items:center;justify-content:center;font-size:17px;font-weight:600;color:var(--ink)}
.arrow-l{left:29px;top:287px;border-radius:0 18px 18px 0}
.arrow-r{left:611px;top:287px;border-radius:18px 0 0 18px}

.show{left:646px;top:170px;width:264px;height:285px;border:1px solid var(--line);border-radius:3px}
.show-thumb{left:10px;top:16px;width:122px;height:73px;background:radial-gradient(ellipse,#5a2a20,#1a0e0b)}
.show-info{left:149px;top:23px;font-size:12px;line-height:17px;color:var(--muted)}
.show-info b{font-weight:400;color:var(--red)}
.about{left:6px;top:106px;width:250px;font-size:12px;color:var(--muted);line-height:14px}
.about p+p{margin-top:12px}
.cast{left:8px;top:174px;font-size:12px;line-height:17px;color:var(--muted)}
.cast b{font-weight:400;color:var(--red)}
.cast .k{display:inline-block;width:65px}
.join{left:24px;top:241px;width:221px;height:33px;border-radius:3px;background:linear-gradient(#8fd136,var(--green-dark));color:var(--white);font-size:16px;display:flex;align-items:center;justify-content:center}

.filters{left:40px;top:497px;width:868px;font-size:13px;color:var(--muted)}
.radio{display:inline-flex;align-items:center;gap:6px;margin-right:40px}
.radio i{width:11px;height:11px;border:1px solid #999;border-radius:50%;display:inline-block;position:relative}
.radio i.on::after{content:"";position:absolute;left:2px;top:2px;width:5px;height:5px;border-radius:50%;background:var(--green)}
.filters .links{position:absolute;right:0;top:0}
.filters .links span{margin-left:56px}

.guide{left:27px;top:539px;width:885px;height:418px;background:var(--grid-bg)}
.row{position:absolute;left:8px;width:871px;background:var(--white);border-radius:3px;display:grid;grid-template-columns:131px 104px 104px 104px 104px 103px 113px 108px}
.row > div{border-left:1px solid #dedede;display:flex;align-items:center;justify-content:center;text-align:center;font-size:11px;line-height:19px;color:var(--muted)}
.row > div:first-child{border-left:0;justify-content:flex-start;padding-left:25px;gap:33px}
.row.head > div{font-size:12.5px;color:var(--ink)}
.box{width:12px;height:12px;border:1px solid #999;background:#f4f4f4;font-size:10px;line-height:10px;color:#335;text-align:center}
.channel{width:46px;font-size:9px;font-weight:600;color:#444;line-height:11px;text-align:center}
.pager{right:10px;top:396px;display:flex;gap:14px}
.pager i{width:16px;height:16px;border-radius:50%;background:#444;color:var(--white);font-style:normal;font-size:9px;display:flex;align-items:center;justify-content:center}

.card{top:989px;width:253px;height:131px;border:1px solid var(--line);border-radius:3px;background:var(--white);font-family:Arimo,Arial,sans-serif}
.card h3{position:absolute;left:48px;top:19px;font:12px "Source Sans 3",sans-serif;color:var(--ink)}
.card .icon{position:absolute;left:11px;top:10px}
.news{left:34px}
.news input{position:absolute;left:16px;top:48px;width:207px;height:32px;border:1px solid var(--line);border-radius:3px}
.subscribe{position:absolute;left:22px;top:92px;width:94px;height:23px;border-radius:12px;background:var(--yellow);font:12px "Source Sans 3",sans-serif;display:flex;align-items:center;justify-content:center}
.feeds{left:334px}
.feeds .txt{position:absolute;left:10px;top:51px;width:240px;font-size:10px;line-height:13px;color:#444}
.feeds a{color:var(--link);text-decoration:none}
.feeds .acts{position:absolute;left:10px;top:103px;font-size:10px;color:#555}
.feeds .acts span{margin-right:16px}
.events{left:643px}
.event-photo{position:absolute;left:6px;top:51px;width:85px;height:64px;background:linear-gradient(135deg,#3a6fb5,#1b2c55 60%,#6b3a6b)}
.events .txt{position:absolute;left:99px;top:51px;width:150px;font-size:10px;line-height:13px;color:#444}
.events .time{position:absolute;left:99px;top:103px;font-size:10px;color:#444}

.footer{left:0;top:1169px;width:935px;text-align:center;font-size:11.5px;color:#444}
</style>
</head>
<body>

<header class="header abs">
  <div class="brand abs">Kluvora</div>
  <form class="search abs"><input value="Enter Text" aria-label="Search"><button type="button">SEARCH</button></form>
  <div class="account abs">Setting<span>|</span>Login<span>|</span>Register<span>|</span>Help</div>
</header>

<nav class="nav abs">
  <a class="active" href="#">HOME</a>
  <a href="#">MY CONVERSATIONS</a>
  <a href="#" style="margin-left:45px">ALL CONVERSATIONS</a>
  <a href="#" style="margin-left:47px">CHANNELS</a>
  <a href="#" style="margin-left:47px">PROGRAMS</a>
</nav>

<main class="panel abs"></main>

<section class="hero abs"></section>
<div class="hero-photo abs" role="img" aria-label="Promotional photo of the band featured in the programme"></div>
<div class="hero-bar abs">
  <div class="title abs">Program Name</div>
  <div class="meta abs">Wed 8.00pm - 9.00 pm<span>|</span>View Conversation<span>|</span>Add Conversation</div>
  <div class="shares abs">
    <div><span class="pill">Like</span><span class="count">3k</span></div>
    <div><span class="pill">Share</span><span class="count">316</span></div>
  </div>
</div>
<div class="arrow-btn arrow-l abs">»</div>
<div class="arrow-btn arrow-r abs">«</div>

<aside class="show abs">
  <div class="show-thumb abs" role="img" aria-label="Thumbnail photo of the show's band"></div>
  <div class="show-info abs"><b>SHOW</b><br>8 00 PM - 9 PM<br>NC1</div>
  <div class="about abs"><p>About This Programme</p><p>Mara Quinn interviews the parents of murdered teenager Elsa.</p></div>
  <div class="cast abs"><b>Cast and Crew</b><br><span class="k">Reporter</span>Tom Ellery<br><span class="k">Presenter</span>Jas Corwin</div>
  <div class="join abs">Join Conversation</div>
</aside>

<div class="filters abs">
  <span class="radio"><i class="on"></i>All Channels</span>
  <span class="radio"><i></i>My Channels</span>
  <div class="links"><span>Add to Channels</span><span>Conversations</span></div>
</div>

<section class="guide abs">
  <div class="row head" style="top:7px;height:43px"><div></div><div>9:00</div><div>9:30</div><div>10:00</div><div>10:30</div><div>11:00</div><div>11:30</div><div>12:00</div></div>
  <div class="row" style="top:52px;height:64px"><div><span class="box">✓</span><span class="channel">Northcast 1</span></div><div>Programe<br>Name</div><div>Programe<br>Name</div><div>Programe<br>Name</div><div>Programe<br>Name</div><div>Programe<br>Name</div><div>Programe<br>Name</div><div>Programe<br>Name</div></div>
  <div class="row" style="top:119px;height:64px"><div><span class="box">✓</span><span class="channel">Northcast 2</span></div><div>Programe<br>Name</div><div>Programe<br>Name</div><div>Programe<br>Name</div><div>Programe<br>Name</div><div>Programe<br>Name</div><div>Programe<br>Name</div><div>Programe<br>Name</div></div>
  <div class="row" style="top:187px;height:64px"><div><span class="box"></span><span class="channel">Vista 1</span></div><div>Programe<br>Name</div><div>Programe<br>Name</div><div>Programe<br>Name</div><div>Programe<br>Name</div><div>Programe<br>Name</div><div>Programe<br>Name</div><div>Programe<br>Name</div></div>
  <div class="row" style="top:254px;height:64px"><div><span class="box"></span><span class="channel">Quadra</span></div><div>Programe<br>Name</div><div>Programe<br>Name</div><div>Programe<br>Name</div><div>Programe<br>Name</div><div>Programe<br>Name</div><div>Programe<br>Name</div><div>Programe<br>Name</div></div>
  <div class="row" style="top:321px;height:64px"><div><span class="box"></span><span class="channel">Fivefold</span></div><div>Programe<br>Name</div><div>Programe<br>Name</div><div>Programe<br>Name</div><div>Programe<br>Name</div><div>Programe<br>Name</div><div>Programe<br>Name</div><div>Programe<br>Name</div></div>
  <div class="pager abs"><i>◀</i><i>▶</i></div>
</section>

<section class="card news abs">
  <svg class="icon" width="30" height="26" viewBox="0 0 30 26"><rect x="1" y="4" width="28" height="20" rx="2" fill="#e8eef7" stroke="#4a6fa5"/><path d="M1 5 L15 16 L29 5" fill="none" stroke="#4a6fa5"/></svg>
  <h3>SUBSCRIBE FOR NEWSLETTER</h3>
  <input aria-label="Email address">
  <div class="subscribe">SUBSCRIBE</div>
</section>

<section class="card feeds abs">
  <svg class="icon" width="30" height="26" viewBox="0 0 30 26"><path d="M4 4 h20 a3 3 0 0 1 3 3 v10 a3 3 0 0 1 -3 3 h-12 l-6 5 v-5 h-2 a3 3 0 0 1 -3 -3 v-10 a3 3 0 0 1 3 -3z" fill="#3aa0d8"/></svg>
  <h3>CHIRPER FEEDS</h3>
  <div class="txt">Lorem ipsum dolor sit amet, consectetuer adipiscing elit. Nam nibh. Nunc varius facilisis eros.<br><a href="#">http://www.loremfeed.net/ut/labore/4et</a></div>
  <div class="acts"><span>2min ago</span><span>reply</span><span>retweet</span><span>favourite</span></div>
</section>

<section class="card events abs">
  <svg class="icon" width="30" height="26" viewBox="0 0 30 26"><rect x="3" y="5" width="24" height="18" rx="4" fill="#e6eef8" stroke="#4a6fa5" stroke-width="2"/><rect x="8" y="9" width="14" height="10" rx="2" fill="#9cc3ea"/></svg>
  <h3>UPCOMING EVENT</h3>
  <div class="event-photo" role="img" aria-label="Photo of a crowd at a live event"></div>
  <div class="txt">Lorem ipsum dolor sit amet, consectetuer adipiscing elit. Nam nibh. Nunc varius facilisis eros.</div>
  <div class="time">8.00 pm &nbsp;- &nbsp;9.00pm</div>
</section>

<footer class="footer abs">© 2012 Kluvora, All rights reserved</footer>

</body>
</html>
```